Birchford Realty Business Card

Business Card:

Somewhere on front of card, please include Broker License Number: 5839162

Website is BirchfordRealty.example

Address is:
7218 Crestover Ave E
Saginaw, MI 48271

I'll let you use creative freedom on the rest; we obviously need Name, Title, Email (@BirchfordRealty.example), Office Phone, Cell Phone.

Don't want any special die-cutting, just a standard size business card.

On the back, include a place for the date and time of an appointment to be written in pen.

Requirements
Must have
• Our logo, attached to email.

```html
<!DOCTYPE html>
<html lang="en">
<head>
<meta charset="utf-8">
<title>Birchford Realty Business Card</title>
<link rel="stylesheet" href="https://fonts.googleapis.com/css2?family=Open+Sans:wght@400;600;700&display=swap">
<style>
  :root {
    --page-bg: #ecedf3;
    --card-grey: #c9cacd;
    --card-grey-light: #d3d4d7;
    --brand-blue: #2b2b7e;
    --stripe-white: #ffffff;
    --text-blue: #2b2b7e;
  }
  html, body {
    margin: 0;
    width: 1200px;
    height: 900px;
    overflow: hidden;
    background: var(--page-bg);
    font-family: "Open Sans", Arial, sans-serif;
  }
  .canvas {
    position: relative;
    width: 1200px;
    height: 900px;
  }
  .card {
    position: absolute;
    left: 285px;
    width: 630px;
    height: 360px;
    border-radius: 22px;
    overflow: hidden;
    box-shadow: 0 6px 18px rgba(40, 40, 80, 0.18);
  }
  .card-front { top: 70px; background: var(--card-grey); }
  .card-back { top: 470px; background: var(--brand-blue); }
  .card-graphic {
    position: absolute;
    inset: 0;
    width: 100%;
    height: 100%;
  }
  .brand-name {
    position: absolute;
    margin: 0;
    font-weight: 700;
    line-height: 1.1;
  }
  .card-front .brand-name {
    left: 36px;
    top: 140px;
    font-size: 30px;
    color: var(--text-blue);
  }
  .card-back .brand-name {
    left: 58px;
    top: 142px;
    font-size: 34px;
    color: var(--stripe-white);
  }
  .contact-block {
    position: absolute;
    left: 310px;
    top: 78px;
    color: var(--text-blue);
    font-size: 15px;
    line-height: 1.45;
  }
  .contact-block p { margin: 0; }
  .company-line { font-weight: 700; font-size: 19px; }
  .license-line { font-weight: 700; font-size: 19px; margin-bottom: 2px !important; }
  .address-line { font-weight: 400; }
  .address-group { margin-bottom: 12px !important; }
  .phone-line { font-weight: 600; }
  .appointment-box {
    position: absolute;
    right: 40px;
    bottom: 36px;
    width: 300px;
    height: 92px;
    background: var(--stripe-white);
  }
</style>
</head>
<body>
<main class="canvas">

  <section class="card card-front" aria-label="Business card front">
    <svg class="card-graphic" viewBox="0 0 630 360" aria-hidden="true">
      <polygon points="0,180 262,180 205,360 0,360" fill="var(--card-grey-light)"/>
      <polygon points="165,0 197,0 264,180 244,180" fill="var(--brand-blue)"/>
      <polygon points="244,180 264,180 207,360 170,360" fill="var(--stripe-white)"/>
    </svg>
    <p class="brand-name">Birchford<br>Realty</p>
    <div class="contact-block">
      <p class="company-line">BirchfordRealty</p>
      <p class="license-line">5839162</p>
      <div class="address-group">
        <p class="address-line">7218 Crestover Ave E</p>
        <p class="address-line">Saginaw, MI 48271</p>
      </div>
      <p class="phone-line">office phone : 555-0142</p>
      <p class="phone-line">cell phone: 555-0187</p>
      <p class="phone-line">email: @BirchfordRealty.example</p>
      <p class="phone-line">web: BirchfordRealty.example</p>
    </div>
  </section>

  <section class="card card-back" aria-label="Business card back">
    <svg class="card-graphic" viewBox="0 0 630 360" aria-hidden="true">
      <polygon points="250,0 275,0 335,70 630,62 630,76 325,86" fill="var(--stripe-white)"/>
    </svg>
    <p class="brand-name">Birchford Realty</p>
    <div class="appointment-box" aria-label="Space for appointment date and time"></div>
  </section>

</main>
</body>
</html>
```